Urgent * Legal Consultant Website Design

Provide a brief overview about your business Hello, website design required for independent legal consultant. Upload your company logo in the brief UPLOADED Specify the main navigation menu of your website (For better reference here's a sample of a website's navigation menu: (http://brovik88.net/wp-content/uploads/2012/css-menu/ 3.jpg) Header menu should include: About Us, Our people, Services and Contact Us Indicate the subpages or the dropdown menu if you have any (Refer to: http://pemtaz.co/wp-content/uploads/2010 /11/nav.jpg) No Subpages in the dropdown Upload to separate file for the text or the content needed for the homepage (This is a helpful supporting file to provide in order for our designers to better understand the elements needed on how to layout your This could be in Word document if you're using Windows or in Pages if you are using Mac. ) GET your legal advice and protect you and your BUSINESS Family Law Debt Recovery Leases Crimes & Traffic, wills Violence Restraining Orders Probate Titles Shariah Law Provide some samples of Web designs you like for better reference (Cite 2 to 3 samples) Website must be clean , simple and display our services in a clear way. Examples: https://cdn.vurdomix.com/wp/wp-content/uploads/sites/2/trosmo-simple-business-wordpress-theme-1024x846.jpg https://cdn.vurdomix.com/wp/wp -content / uploads / sites / 2 / pelinor-creative-studio-wp-website-template-1024x791.jpg Upload photos or files you would like to include in the design, or make mention if you are open to use stock photos Open to Use stock photos
Number of Pages Required
1 page
Look and feel
Each slider illustrates characteristics of the customer's brand and the style your logo design should communicate.

```html
<!DOCTYPE html>
<html lang="en">
<head>
<meta charset="utf-8">
<title>Lexmoor Counsel</title>
<link href="https://fonts.googleapis.com/css2?family=Tinos:wght@700&family=Mulish:wght@400;600;700;800&display=swap" rel="stylesheet">
<style>
:root{
  --red:#c8302c;
  --red-dark:#922724;
  --ink:#1a1a1a;
  --text:#444;
  --muted:#8a8a8a;
  --section:#f4f4f4;
  --gold:#f2d57a;
  --white:#fff;
  --button-grey:#cfcfcf;
}
*{margin:0;padding:0;box-sizing:border-box}
html,body{width:1200px;height:1200px;overflow:hidden;background:var(--white)}
body{font-family:"Mulish",sans-serif;color:var(--text);position:relative}
.site{position:absolute;left:297px;top:0;width:606px;height:1200px}
.abs{position:absolute}
.brand{font-family:"Tinos",serif;font-weight:700;color:var(--ink);white-space:nowrap;letter-spacing:.2px}

/* top bar */
.social{display:flex;gap:3px}
.social span{width:9px;height:9px;background:#555;border-radius:2px;display:block}
.topbar .phone{right:25px;top:62px;font-size:6px;color:#777;display:flex;align-items:center;gap:3px}
.topbar .phone svg{width:7px;height:7px}
.rule{left:0;top:74px;width:606px;height:1px;background:#e6e6e6}

/* header */
.header-brand{left:30px;top:90px;font-size:14px}
.nav{top:97px;left:354px;display:flex;gap:17px;font-size:5.6px;font-weight:700;color:var(--ink);letter-spacing:.2px}
.nav .active{color:var(--red)}

/* hero */
.hero{left:0;top:116px;width:606px;height:240px;background:linear-gradient(90deg,#8f8f8a 0%,#b5b7b3 35%,#9a9c98 60%,#6d6f6c 100%)}
.hero h1{position:absolute;left:26px;top:54px;font-family:"Tinos",serif;font-weight:700;font-size:16px;line-height:24px;color:var(--ink)}
.btn-red{background:var(--red);color:var(--white);font-weight:700;font-size:6.4px;display:flex;align-items:center;justify-content:center;letter-spacing:.2px}
.hero .btn-red{position:absolute;left:24px;top:142px;width:109px;height:22px}

/* services */
.services{left:0;top:356px;width:606px;height:362px;background:var(--section)}
.service{position:absolute;width:130px}
.service .thumb{position:absolute;left:28px;width:74px;height:74px;border-radius:50%}
.service .card{position:absolute;left:0;width:130px;height:59px;background:var(--white);padding:5px 12px 0 15px}
.service h3{font-size:6.8px;font-weight:800;color:var(--ink);margin-bottom:1px}
.service p{font-size:6.6px;line-height:8.3px;color:#555}
.service .btn-red{width:52px;height:10px;font-size:5.2px;margin-top:3px}

/* about */
.about-brand{left:197px;top:789px;font-size:14px}
.about-photo{left:0;top:844px;width:322px;height:140px;background:linear-gradient(100deg,#1e1b1b 0%,#2b2424 40%,#f6ebe6 75%,#ffffff 100%)}
.about h2{left:414px;top:781px;font-size:10px;font-weight:600;color:var(--muted);white-space:nowrap}
.about h2 b{color:var(--ink);font-weight:800}
.features{left:425px;top:815px;list-style:none}
.features li{position:absolute;left:0;font-size:7px;color:#333;white-space:nowrap;display:flex;align-items:center;gap:11px}
.features li i{width:4px;height:7px;border:1.5px solid var(--red);border-right:none;display:block}
.btn-grey{left:414px;top:926px;width:90px;height:19px;background:var(--button-grey);color:#444;font-size:7px;display:flex;align-items:center;justify-content:center}

/* footer */
.footer{left:0;top:984px;width:606px;height:158px}
.footer .bg{position:absolute;inset:0}
.footer .social{position:absolute;left:288px;top:10px}
.footer .social span{width:10px;height:10px;background:var(--white)}
.panel{position:absolute;top:38px;height:80px;background:var(--white)}
.testimonial{left:25px;width:276px}
.testimonial .avatar{position:absolute;left:8px;top:8px;width:24px;height:24px;border-radius:50%;background:linear-gradient(#7a8aa0,#3d3f48)}
.testimonial .quote{position:absolute;left:37px;top:22px;font-family:"Tinos",serif;font-size:9px;color:#555}
.testimonial p{position:absolute;left:46px;top:32px;font-size:5.4px;color:#555;white-space:nowrap}
.testimonial .who{position:absolute;left:196px;top:43px;font-size:5.4px;line-height:8px;color:#333}
.testimonial .who span{color:var(--red);display:block}
.dots{position:absolute;left:123px;top:64px;display:flex;gap:2px}
.dots i{width:5px;height:5px;border-radius:50%;background:#999;display:block}
.dots i:first-child{background:var(--red)}
.partners{left:305px;width:276px;display:flex;align-items:center;justify-content:space-around}
.partners .brand{font-size:11px}
.footer-brand{left:24px;top:1123px;font-size:8px;color:var(--white)}
.copyright{right:55px;top:1127px;font-family:"Tinos",serif;font-size:5.6px;color:var(--white)}
.accent{left:0;top:1140px;width:606px;height:2px;background:var(--gold)}
</style>
</head>
<body>
<div class="site">

  <div class="topbar">
    <div class="social abs" style="left:31px;top:62px"><span></span><span></span><span></span></div>
    <div class="phone abs">
      <svg viewBox="0 0 10 10"><rect width="10" height="10" rx="2" fill="#c8302c"/><path d="M3 2.5c.5 2 1.8 3.6 4.5 4.8l.7-1-1.3-.8-.6.6C5.4 5.5 4.6 4.7 4 3.8l.6-.6-.8-1.3z" fill="#fff"/></svg>
      +610 5550 1234
    </div>
    <div class="rule abs"></div>
  </div>

  <header>
    <div class="brand header-brand abs">LEXMOOR COUNSEL</div>
    <nav class="nav abs">
      <span class="active">HOME</span><span>ABOUT US</span><span>OUR PEOPLE</span><span>SERVICES ⌄</span><span>CONTACT US</span>
    </nav>
  </header>

  <section class="hero abs" role="img" aria-label="Photo of a senior lawyer in shirt and tie by an office window">
    <h1>GET your legal advice and<br>protect you and your<br>BUSINESS</h1>
    <div class="btn-red">CONTACT US</div>
  </section>

  <section class="services abs">
    <div class="service" style="left:24px;top:36px">
      <div class="thumb" role="img" aria-label="Photo of a couple" style="top:0;background:radial-gradient(circle at 50% 40%,#c9b7a8,#7a2a2a 70%,#5a4a44)"></div>
      <div class="card" style="top:80px"><h3>Family Law</h3><p>Our family lawyers know that divorce and separation can be one of the most stressful time...</p><div class="btn-red">READ MORE</div></div>
    </div>
    <div class="service" style="left:166px;top:36px">
      <div class="thumb" role="img" aria-label="Photo of a man seated by a concrete wall" style="top:0;background:radial-gradient(circle at 50% 50%,#8a8c8a,#5d605e 70%)"></div>
      <div class="card" style="top:80px"><h3>Debt Recovery</h3><p>Our family lawyers know that divorce and separation can be one of the most stressful time...</p><div class="btn-red">READ MORE</div></div>
    </div>
    <div class="service" style="left:308px;top:36px">
      <div class="thumb" role="img" aria-label="Photo of hands signing a document" style="top:0;background:linear-gradient(160deg,#2b2b2b 0%,#6a5a55 40%,#e8e8e8 60%,#c27a6e 100%)"></div>
      <div class="card" style="top:80px"><h3>Leases</h3><p>Our family lawyers know that divorce and separation can be one of the most stressful time...</p><div class="btn-red">READ MORE</div></div>
    </div>
    <div class="service" style="left:451px;top:36px">
      <div class="thumb" role="img" aria-label="Photo of a crime scene outline on a chequered floor" style="top:0;background:radial-gradient(circle,#8a2a2a,#2a3848 75%)"></div>
      <div class="card" style="top:80px"><h3>Crimes &amp; Traffic, Wills</h3><p>Our family lawyers know that divorce and separation can be one of the most stressful time...</p><div class="btn-red">READ MORE</div></div>
    </div>

    <div class="service" style="left:24px;top:193px">
      <div class="thumb" role="img" aria-label="Photo illustrating domestic conflict" style="top:0;background:radial-gradient(circle,#c9a79a,#5c5a5c 75%)"></div>
      <div class="card" style="top:80px"><h3>Violence Restraining Orders</h3><p>Our family lawyers know that divorce and separation can be one of the most stressful time...</p><div class="btn-red">READ MORE</div></div>
    </div>
    <div class="service" style="left:166px;top:193px">
      <div class="thumb" role="img" aria-label="Photo of a pen writing a will" style="top:0;background:linear-gradient(135deg,#ffffff 0%,#f0f0f0 55%,#9a9a9a 100%)"></div>
      <div class="card" style="top:80px"><h3>Probate</h3><p>Our family lawyers know that divorce and separation can be one of the most stressful time...</p><div class="btn-red">READ MORE</div></div>
    </div>
    <div class="service" style="left:308px;top:193px">
      <div class="thumb" role="img" aria-label="Photo of a judge's gavel on banknotes" style="top:0;background:radial-gradient(circle at 40% 60%,#c89a6a,#e9e9e9 70%)"></div>
      <div class="card" style="top:80px"><h3>Strata Titles</h3><p>Our family lawyers know that divorce and separation can be one of the most stressful time...</p><div class="btn-red">READ MORE</div></div>
    </div>
    <div class="service" style="left:451px;top:193px">
      <div class="thumb" role="img" aria-label="Photo of a justice statue against blue sky" style="top:0;background:radial-gradient(circle at 55% 55%,#9aa8c0,#2d4f96 70%)"></div>
      <div class="card" style="top:80px"><h3>Shariah Law</h3><p>Our family lawyers know that divorce and separation can be one of the most stressful time...</p><div class="btn-red">READ MORE</div></div>
    </div>
  </section>

  <section class="about">
    <div class="brand about-brand abs">LEXMOOR COUNSEL</div>
    <div class="about-photo abs" role="img" aria-label="Photo of an outstretched hand in a dark suit sleeve presenting the firm name"></div>
    <h2 class="abs"><b>OUR</b> Work Is Your Satisfaction</h2>
    <ul class="features abs">
      <li style="top:1px"><i></i>The Best Deals</li>
      <li style="top:25px"><i></i>Professionals Experience</li>
      <li style="top:51px"><i></i>Contact Fast</li>
      <li style="top:79px"><i></i>Secure Business</li>
    </ul>
    <div class="btn-grey abs">More Services</div>
  </section>

  <footer class="footer abs">
    <svg class="bg" viewBox="0 0 606 158" preserveAspectRatio="none">
      <rect width="606" height="158" fill="#c8302c"/>
      <path d="M0 0 H606 V38 L0 135 Z" fill="#922724"/>
    </svg>
    <div class="social"><span></span><span></span><span></span></div>
    <div class="panel testimonial">
      <div class="avatar" role="img" aria-label="Client portrait"></div>
      <div class="quote">❝</div>
      <p>Thank for the help with my father, we appreciate the deal so much!</p>
      <div class="who"><span>-Dan Morlen</span>-Engineer</div>
      <div class="dots"><i></i><i></i><i></i></div>
    </div>
    <div class="panel partners">
      <span class="brand">LEXMOOR COUNSEL</span>
      <span class="brand">LEXMOOR COUNSEL</span>
    </div>
  </footer>
  <div class="brand footer-brand abs">LEXMOOR COUNSEL</div>
  <div class="copyright abs">© 2018 All Rights Reserved</div>
  <div class="accent abs"></div>

</div>
</body>
</html>
```